Packaging for eco friendly dog poo bags

Hello, I'm looking for a creative designer for packaging design and bags design for eco friendly dog poo bags.

-I need the ( box ) and the ( bags ) design.
-I need full wrap and print ready version for all faces and angles.
-I need a 3D presentation ( mockup )

I have attached the supplier sizes with instructions for the box.

-I'm looking for someone who is creative and can deliver asap.

My budget around : 50-70$
Deadline : 4 days.

```html
<!DOCTYPE html>
<html lang="en">
<head>
<meta charset="utf-8">
<title>Leafwalk Co. – Compostable Dog Poo Bags</title>
<link rel="stylesheet" href="https://fonts.googleapis.com/css2?family=Luckiest+Guy&family=Fredoka:wght@500;600;700&display=swap">
<style>
  :root {
    --bg: #e9e9e9;
    --tab-green: #3f8c47;
    --tab-hole: #f2f2f2;
    --kraft: #ead7b6;
    --kraft-light: #f3e6cc;
    --dot-green: #4c9a4b;
    --window-green: #79c23d;
    --window-edge: #c9793c;
    --grass: #5fb43a;
    --grass-dark: #3f8f2c;
    --title-green: #8cd12f;
    --ink: #1d1d1b;
    --white: #ffffff;
    --teal-ink: #2f5e5c;
  }
  * { box-sizing: border-box; margin: 0; padding: 0; }
  html, body { width: 1146px; height: 1200px; overflow: hidden; }
  body { background: var(--bg); font-family: "Fredoka", sans-serif; position: relative; }

  .box { position: absolute; left: 415px; top: 195px; width: 315px; }

  .hang-tab {
    position: relative; height: 121px; background: var(--tab-green);
  }
  .hang-tab__hole {
    position: absolute; left: 86px; top: 48px; width: 143px; height: 23px;
    background: var(--tab-hole); border-radius: 12px;
  }

  .front {
    position: relative; height: 658px; overflow: hidden;
    background: var(--kraft);
  }
  .front__art {
    position: absolute; inset: 0;
    background:
      linear-gradient(180deg, var(--dot-green) 0%, rgba(76,154,75,0.55) 14%, rgba(234,215,182,0) 34%),
      radial-gradient(circle at 50% 70%, var(--kraft-light) 0%, var(--kraft) 60%);
  }

  .window {
    position: absolute; left: 47px; top: 155px; width: 210px; height: 261px;
    background: var(--window-green); border-radius: 6px;
    box-shadow: inset 0 0 0 2px var(--window-edge);
  }

  .brand-badge {
    position: absolute; left: 64px; top: 38px; width: 174px; height: 162px;
    background: var(--white); border-radius: 26px;
    box-shadow: 0 2px 4px rgba(0,0,0,0.12);
  }
  .brand-badge__art {
    position: absolute; left: 30px; top: 8px; width: 114px; height: 112px;
    border-radius: 50%;
    background: radial-gradient(circle, #cfd8d4 0%, #eef0ee 70%, var(--white) 100%);
  }
  .brand-badge__name {
    position: absolute; left: 0; right: 0; top: 128px; text-align: center;
    font-family: "Fredoka", sans-serif; font-weight: 700; font-size: 17px;
    letter-spacing: 0.5px; color: var(--teal-ink); text-transform: uppercase;
  }

  .title {
    position: absolute; left: 0; right: 0; top: 418px; text-align: center;
    font-family: "Luckiest Guy", sans-serif; line-height: 1; text-transform: uppercase;
  }
  .title__line { display: block; font-size: 29px; -webkit-text-stroke: 1.5px var(--ink); }
  .title__line--green { color: var(--title-green); }
  .title__line--white { color: var(--white); margin-top: 8px; }

  .grass { position: absolute; left: 0; bottom: 0; width: 315px; height: 110px; }

  .claim {
    position: absolute; top: 518px; width: 84px; height: 44px;
    background: var(--white); border: 2px solid var(--ink); border-radius: 50%;
    display: flex; align-items: center; justify-content: center; text-align: center;
    font-weight: 700; font-size: 8.5px; line-height: 1.1; color: var(--ink);
    text-transform: uppercase; padding: 0 10px;
  }
  .claim--toxins { left: 46px; }
  .claim--plant { left: 145px; }
  .claim__icon { position: absolute; right: -4px; top: -10px; width: 22px; height: 22px; }

  .count {
    position: absolute; left: 3px; top: 600px; width: 48px; height: 48px;
    background: var(--ink); border-radius: 50%; color: var(--white);
    display: flex; flex-direction: column; align-items: center; justify-content: center;
    font-family: "Luckiest Guy", sans-serif; line-height: 0.9;
  }
  .count__num { font-size: 19px; }
  .count__unit { font-size: 9px; }

  .website {
    position: absolute; left: 68px; top: 610px;
    font-weight: 600; font-size: 8px; color: var(--white); text-transform: uppercase;
    letter-spacing: 0.3px;
  }

  .mascot {
    position: absolute; left: 226px; top: 535px; width: 76px; height: 118px;
    border-radius: 40% 40% 20% 20%;
    background: linear-gradient(180deg, #f7f2ea 0%, #e8d9c4 100%);
  }
</style>
</head>
<body>
  <div class="box">
    <div class="hang-tab"><div class="hang-tab__hole"></div></div>

    <div class="front">
      <div class="front__art" role="img" aria-label="Green halftone dots fading into a kraft sunburst background"></div>

      <div class="window"></div>

      <div class="brand-badge">
        <div class="brand-badge__art" role="img" aria-label="Engraved-style illustration of a smiling dog with sun rays"></div>
        <div class="brand-badge__name">Leafwalk Co.</div>
      </div>

      <h1 class="title">
        <span class="title__line title__line--green">Compostable</span>
        <span class="title__line title__line--white">Dog Poo Bags</span>
      </h1>

      <svg class="grass" viewBox="0 0 315 110" role="img" aria-label="Green grass band with small flowers">
        <path d="M0 40 C60 30 120 18 180 26 C230 32 280 40 315 34 L315 110 L0 110 Z" fill="var(--grass)"/>
        <path d="M0 100 L315 100 L315 110 L0 110 Z" fill="var(--grass-dark)"/>
      </svg>

      <div class="claim claim--toxins">No toxins or microplastic
        <svg class="claim__icon" viewBox="0 0 22 22"><circle cx="11" cy="11" r="10" fill="var(--ink)"/><path d="M7 15 C7 9 11 6 16 6 C16 11 13 15 7 15 Z" fill="var(--title-green)"/></svg>
      </div>
      <div class="claim claim--plant">Plant based material
        <svg class="claim__icon" viewBox="0 0 22 22"><circle cx="11" cy="11" r="10" fill="var(--white)"/><path d="M6 16 C6 9 11 5 17 5 C17 11 13 16 6 16 Z" fill="var(--grass)"/></svg>
      </div>

      <div class="count"><span class="count__num">60</span><span class="count__unit">Bags</span></div>

      <div class="website">www.leafwalkbags.co.uk</div>

      <div class="mascot" role="img" aria-label="Cartoon puppy with a red collar sitting on the grass"></div>
    </div>
  </div>
</body>
</html>
```